Robotic consulting firm needs a Powerpoint Template

I'm looking for a powerpoint template for my consulting business. We are in the robotic field and needs to present project concept or robotic cell layout to the client. I'm looking for a design that is professionnal and using my logo. Our color is purple, but I don't want to overuse the color everywhere, it needs to look professionnal for the engineer field. Color code is 9F35D8

```html
<!DOCTYPE html>
<html lang="en">
<head>
<meta charset="UTF-8">
<title>Novaris Presentation Template</title>
<link href="https://fonts.googleapis.com/css2?family=Krona+One&family=Michroma&family=Archivo:wght@400;700&display=swap" rel="stylesheet">
<style>
  :root {
    --brand: #9f35d8;
    --ink: #0a0a0a;
    --board: #999999;
    --paper: #ffffff;
    --steel: #c9cbd6;
    --mist: #eef0f5;
  }
  * { margin: 0; padding: 0; box-sizing: border-box; }
  html, body { width: 1200px; height: 1200px; overflow: hidden; background: var(--board); }
  .board { position: relative; width: 1200px; height: 1200px; }
  .slide { position: absolute; left: 163px; width: 874px; height: 490px; background: var(--paper); overflow: hidden; }
  .slide--cover { top: 86px; }
  .slide--content { top: 620px; }

  .hero-photo {
    position: absolute; right: 0; top: 0; width: 70%; height: 100%;
    background:
      radial-gradient(ellipse 40% 55% at 78% 60%, rgba(159,53,216,0.55), transparent 70%),
      radial-gradient(ellipse 50% 60% at 70% 45%, #b7b9c8, transparent 75%),
      linear-gradient(90deg, var(--paper) 0%, rgba(255,255,255,0.6) 30%, var(--mist) 55%, #d5d7e2 100%);
  }
  .hero-photo::after {
    content: ""; position: absolute; inset: 0;
    background: linear-gradient(180deg, transparent 60%, rgba(255,255,255,0.5) 100%),
                linear-gradient(90deg, var(--paper) 0%, transparent 35%);
  }

  .brand { position: absolute; display: flex; align-items: center; font-family: "Krona One", sans-serif; color: var(--brand); }
  .brand__mark { background: var(--brand); }
  .slide--cover .brand { left: 232px; top: 178px; gap: 12px; font-size: 20px; letter-spacing: 4px; left: 68px; }
  .slide--cover .brand__mark { width: 44px; height: 44px; }

  .cover-kicker { position: absolute; left: 69px; top: 337px; font-family: "Michroma", sans-serif; font-size: 20px; color: var(--brand); }
  .cover-rule { position: absolute; left: 69px; top: 366px; width: 372px; height: 1px; background: var(--ink); }
  .cover-title { position: absolute; left: 69px; top: 372px; font-family: "Krona One", sans-serif; font-size: 30px; color: var(--ink); white-space: nowrap; letter-spacing: 0.5px; }
  .cover-title-rule { position: absolute; left: 69px; top: 411px; width: 530px; height: 1px; background: var(--ink); }

  .content-photo-bg {
    position: absolute; right: 0; top: 0; width: 65%; height: 100%;
    background:
      radial-gradient(ellipse 45% 60% at 80% 55%, #e4e5ec, transparent 75%),
      linear-gradient(90deg, var(--paper) 0%, rgba(245,246,250,0.9) 40%, #ecedf3 100%);
  }
  .content-rule { position: absolute; left: 37px; top: 49px; width: 1px; height: 328px; background: var(--ink); }
  .content-title { position: absolute; left: 54px; top: 44px; font-family: "Krona One", sans-serif; font-size: 18px; color: var(--ink); white-space: nowrap; }
  .content-kicker { position: absolute; left: 54px; top: 72px; font-family: "Michroma", sans-serif; font-size: 15px; color: var(--brand); }
  .content-body { position: absolute; left: 54px; top: 122px; width: 330px; font-family: "Archivo", sans-serif; font-size: 10px; line-height: 13px; color: var(--ink); }
  .content-body p + p { margin-top: 13px; }

  .figure { position: absolute; }
  .figure--cell {
    left: 537px; top: 93px; width: 257px; height: 143px;
    background:
      radial-gradient(ellipse 35% 45% at 50% 65%, rgba(159,53,216,0.6), transparent 70%),
      linear-gradient(180deg, #d9dae2 0%, #f1f1f5 50%, #cfd0da 100%);
  }
  .figure--line {
    left: 437px; top: 262px; width: 282px; height: 157px;
    background:
      radial-gradient(ellipse 30% 30% at 50% 40%, #f4eefa, transparent 70%),
      linear-gradient(180deg, #b48fd0 0%, #dccdea 45%, #c6a8de 100%);
  }

  .slide--content .brand { left: 37px; top: 444px; gap: 7px; font-size: 10px; letter-spacing: 2px; }
  .slide--content .brand__mark { width: 14px; height: 14px; }
</style>
</head>
<body>
<main class="board">
  <section class="slide slide--cover">
    <div class="hero-photo" role="img" aria-label="Industrial robotic arm with purple accents in a bright factory, fading into white"></div>
    <div class="brand"><span class="brand__mark"></span><span class="brand__name">NOVARIS</span></div>
    <p class="cover-kicker">Lorem Ipsum Dolor</p>
    <div class="cover-rule"></div>
    <h1 class="cover-title">LOREM IPSUM DOLOR</h1>
    <div class="cover-title-rule"></div>
  </section>

  <section class="slide slide--content">
    <div class="content-photo-bg" role="img" aria-label="Faint robotic arm in a light factory setting"></div>
    <div class="content-rule"></div>
    <h2 class="content-title">LOREM IPSUM DOLOR</h2>
    <p class="content-kicker">Lorem Ipsum Dolor</p>
    <div class="content-body">
      <p>Lorem ipsum dolor sit amet, consectetur adipiscing elit, sed do eiusmod tempor incididunt ut labore et dolore magna aliqua. Quis ipsum suspendisse ultrices gravida. Risus commodo viverra maecenas accumsan lacus vel facilisis.</p>
      <p>Lorem ipsum dolor sit amet, consectetur adipiscing elit, sed do eiusmod tempor incididunt ut labore et dolore magna aliqua. Quis ipsum suspendisse ultrices gravida. Risus commodo viverra maecenas accumsan lacus vel facilisis.</p>
      <p>Lorem ipsum dolor sit amet, consectetur adipiscing elit, sed do eiusmod tempor incididunt ut labore et dolore magna aliqua. Quis ipsum suspendisse ultrices gravida. Risus commodo viverra maecenas accumsan lacus vel facilisis.</p>
    </div>
    <div class="figure figure--cell" role="img" aria-label="Robotic cell with a single white robot arm in a clean room lit purple"></div>
    <div class="figure figure--line" role="img" aria-label="Automated production hall with several robot arms under purple lighting"></div>
    <div class="brand"><span class="brand__mark"></span><span class="brand__name">NOVARIS</span></div>
  </section>
</main>
</body>
</html>
```